Business Card for Coach - ready to print

Design Business Card ready to order prints www.lukasbrenner.coach

* An Overview / Background of the Business & Services
· Coaching
· Personal growth
* The Target Market / Audience you are trying to reach
· private person in different roles (self, familiy, business role)s
* Design Specifics; any preferences or ideas for Style, Colour, Imagery, etc
· See www.lukasbrenner.coach
· "simple" design
· (small) element of surprise / unusual element

* Information that will be placed in the Business Card
· Beratung und Coaching
· Address: Lukas Brenner, Talmatt 42, CH-8531 Seewald, Mobile +41 76 254 63 07
* Do you have an existing website or Facebook page where designers can learn more about your company?
· lukasbrenner.coach

Target Market(s)

private person in different roles (self, familiy, business role)

Industry/Entity Type

Life Coaching

Contact Information for Business Card

Lukas Brenner
Talmatt 42
CH-8531 Seewald

Mobile: +41 76 254 63 07
Email: lubr@sonnwelt.ch
www.lukasbrenner.coach

Font styles to use
Sans Serif

Colors

Designer to choose colors to be used in the design.

Requirements
Must have
• "simple" design
• element of surprise / unusual element
• Beratung & Coaching
• see www.lukasbrenner.coach for colors and so...
Nice to have
• TA Symbol (three rings on top of each other) - unsual presentation
• QR Code of Website (see if it fits in and still looks good).

```html
<!DOCTYPE html>
<html lang="de">
<head>
<meta charset="utf-8">
<title>Lukas Brenner – Beratung &amp; Coaching</title>
<link rel="stylesheet" href="https://fonts.googleapis.com/css2?family=Montserrat:wght@400;500;600&family=Oswald:wght@300;400&display=swap">
<style>
  :root{
    --stage:#1e2227;
    --paper:#ffffff;
    --sky:#2fa7e0;
    --sky-deep:#2590d2;
    --signal:#c01d2a;
    --slate:#3a3b3d;
    --ink-light:#ffffff;
  }
  *{margin:0;padding:0;box-sizing:border-box}
  html,body{width:1200px;height:900px;overflow:hidden;background:var(--stage)}
  .stage{position:relative;width:1200px;height:900px}
  .card{position:absolute;left:250px;width:700px;height:400px;overflow:hidden;border-radius:3px;box-shadow:0 10px 30px rgba(0,0,0,.45)}
  .card--front{top:30px;background:var(--paper)}
  .card--back{top:470px;background:var(--slate)}

  .card__band{position:absolute;left:0;right:0;top:190px;bottom:0;background:linear-gradient(15deg,var(--sky-deep),var(--sky))}

  .brand{position:absolute;display:flex;align-items:center;gap:10px;font-family:"Montserrat",sans-serif;font-weight:600;color:var(--sky);letter-spacing:.5px}
  .brand__dot{width:14px;height:14px;border-radius:50%;background:var(--signal)}
  .card--front .brand{left:58px;top:52px;font-size:30px}
  .tagline{position:absolute;font-family:"Oswald",sans-serif;font-weight:300;text-transform:uppercase;letter-spacing:1px}
  .card--front .tagline{left:58px;top:100px;font-size:22px;color:var(--signal)}

  .contact{position:absolute;right:44px;top:210px;text-align:right;color:var(--ink-light);font-family:"Montserrat",sans-serif}
  .contact__name{font-size:27px;font-weight:400;letter-spacing:2px;text-transform:uppercase;margin-bottom:4px}
  .contact__role{font-size:16px;margin-bottom:10px}
  .contact__line{font-size:15px;line-height:24px;display:flex;justify-content:flex-end;align-items:center;gap:8px}
  .contact__icon{width:16px;height:16px}
  .contact__line--plain{padding-right:24px}

  .card--back .brand{left:0;right:0;top:150px;justify-content:center;font-size:40px}
  .card--back .brand__dot{background:var(--sky);width:18px;height:18px}
  .card--back .tagline{left:0;right:0;top:215px;text-align:center;font-size:24px;color:var(--ink-light)}
</style>
</head>
<body>
<main class="stage">
  <section class="card card--front" aria-label="Visitenkarte Vorderseite">
    <div class="card__band" role="img" aria-label="Geschwungene Welle in Blau mit roter Linie"></div>
    <div class="brand"><span class="brand__name">Lukas Brenner</span><span class="brand__dot"></span></div>
    <p class="tagline">Beratung &amp; Coaching</p>
    <div class="contact">
      <p class="contact__name">Lukas Brenner</p>
      <p class="contact__role">President</p>
      <p class="contact__line contact__line--plain">Talmatt 42</p>
      <p class="contact__line contact__line--plain">CH-8531 Seewald</p>
      <p class="contact__line">+41 76 254 63 07
        <svg class="contact__icon" viewBox="0 0 16 16"><circle cx="8" cy="8" r="7" fill="none" stroke="#fff" stroke-width="1.3"/><path d="M5.5 4.5l1.5 0 .6 1.8-1 .8a5 5 0 0 0 2.3 2.3l.8-1 1.8.6v1.5c-3.5.3-6.3-2.5-6-6z" fill="#fff"/></svg>
      </p>
      <p class="contact__line">lubr@sonnwelt.ch
        <svg class="contact__icon" viewBox="0 0 16 16"><rect x="1.5" y="3.5" width="13" height="9" fill="none" stroke="#fff" stroke-width="1.3"/><path d="M1.5 3.5l6.5 5 6.5-5" fill="none" stroke="#fff" stroke-width="1.3"/></svg>
      </p>
      <p class="contact__line">www.lukasbrenner.coach
        <svg class="contact__icon" viewBox="0 0 16 16"><circle cx="8" cy="8" r="7" fill="#fff"/><g fill="none" stroke="var(--sky)" stroke-width="1"><ellipse cx="8" cy="8" rx="3" ry="7"/><path d="M1 8h14M2.5 4.5h11M2.5 11.5h11"/></g></svg>
      </p>
    </div>
  </section>

  <section class="card card--back" aria-label="Visitenkarte Rückseite">
    <div class="brand"><span class="brand__name">Lukas Brenner</span><span class="brand__dot"></span></div>
    <p class="tagline">Beratung &amp; Coaching</p>
  </section>
</main>
</body>
</html>
```